Massage Therapy and Personal Training Business Card (RT Restful)

I need a logo design based in Washington. The company is called RT Restful. RT are my initials. I specialize in massage therapy and personal training and general wellness of my clients. I've tried getting designs but haven't quite yet found what I'm looking for. I'm not inclined to a certain color yet but some color that resembles wellness such as light blue and white or green and white. Again, I'm not really picky about that. Thank you in advance

Industry/Entity Type

Business

Contact Information for Business Card

Have the description on one side and space for writing information on the back side such as number, appt, etc. I have an example attached. I see a lot of these card. I dont want the exact one, but something similar. Simple, professional and elegant.

Colors

Designer to choose colors to be used in the design.

Requirements
Must have
• Space on the back side to write
• A professional, elegant look
Should not have
• cartoon like style.

```html
<!DOCTYPE html>
<html lang="en">
<head>
<meta charset="utf-8">
<title>RT Restful Business Card</title>
<link href="https://fonts.googleapis.com/css2?family=Roboto:wght@400;500&family=Ubuntu:wght@400;500&display=swap" rel="stylesheet">
<style>
  :root {
    --page-bg: #eef1f4;
    --ink-blue: #2b5d9c;
    --deep-blue: #34619f;
    --sky-blue: #1f9ad6;
    --sea-green: #2aa6c9;
    --mist: #d3e5f4;
    --rule: rgba(43, 93, 156, 0.35);
    --white: #ffffff;
  }
  * { box-sizing: border-box; margin: 0; padding: 0; }
  html, body { width: 1200px; height: 891px; overflow: hidden; }
  body {
    background: var(--page-bg);
    display: flex;
    align-items: center;
    justify-content: center;
    gap: 40px;
  }
  .card {
    position: relative;
    width: 520px;
    height: 297px;
    border-radius: 4px;
    overflow: hidden;
    box-shadow: 0 6px 18px rgba(30, 50, 80, 0.18);
  }
  /* Front */
  .card-front .card-photo {
    position: absolute;
    inset: 0;
    background: linear-gradient(160deg, var(--deep-blue) 0%, #2c7fc0 45%, var(--sea-green) 75%, var(--sky-blue) 100%);
  }
  .front-content {
    position: absolute;
    left: 48px;
    top: 92px;
    color: var(--white);
    font-family: "Roboto", sans-serif;
  }
  .brand-name {
    font-size: 64px;
    font-weight: 500;
    line-height: 1;
  }
  .brand-tagline {
    margin-top: 10px;
    font-size: 19px;
    font-weight: 500;
    line-height: 1.3;
  }
  /* Back */
  .card-back {
    background: linear-gradient(100deg, var(--mist) 0%, #eaf2fa 35%, var(--white) 60%);
    font-family: "Ubuntu", sans-serif;
    color: var(--ink-blue);
  }
  .card-back .leaf-field {
    position: absolute;
    left: 0; top: 0;
    width: 200px; height: 130px;
    background: radial-gradient(ellipse at 45% 50%, rgba(140, 165, 200, 0.3), rgba(255,255,255,0) 70%);
  }
  .writing-space {
    position: absolute;
    left: 22px;
    top: 150px;
    width: 160px;
    list-style: none;
  }
  .writing-line {
    height: 30px;
    border-bottom: 1px solid var(--rule);
  }
  .holder-name {
    position: absolute;
    left: 210px;
    top: 26px;
    font-size: 38px;
    font-weight: 500;
    line-height: 1;
  }
  .holder-role {
    position: absolute;
    left: 232px;
    top: 68px;
    font-size: 17px;
  }
  .contact-list {
    position: absolute;
    left: 200px;
    top: 112px;
    list-style: none;
  }
  .contact-item {
    display: flex;
    align-items: center;
    gap: 12px;
    height: 33px;
    font-size: 16px;
    white-space: nowrap;
  }
  .contact-item.small { font-size: 13px; }
  .contact-icon { width: 24px; height: 24px; flex: none; }
</style>
</head>
<body>
  <section class="card card-front">
    <div class="card-photo" role="img" aria-label="Photograph of a calm blue lake with trees on the shore"></div>
    <div class="front-content">
      <h1 class="brand-name">RT Restful</h1>
      <p class="brand-tagline">massage therapy and personal training<br>and general wellness</p>
    </div>
  </section>

  <section class="card card-back">
    <div class="leaf-field" role="img" aria-label="Scattered falling leaves decoration"></div>
    <ul class="writing-space" aria-label="Space to write appointment details">
      <li class="writing-line"></li>
      <li class="writing-line"></li>
      <li class="writing-line"></li>
      <li class="writing-line"></li>
    </ul>
    <h2 class="holder-name">Your Name</h2>
    <p class="holder-role">Job Role</p>
    <ul class="contact-list">
      <li class="contact-item small">
        <svg class="contact-icon" viewBox="0 0 24 24" fill="none" stroke="#2b5d9c" stroke-width="1.4"><circle cx="12" cy="12" r="11"/><path d="M12 18s-4-4.5-4-7.5a4 4 0 0 1 8 0c0 3-4 7.5-4 7.5z"/><circle cx="12" cy="10.5" r="1.4"/></svg>
        Street Address 1480 Cedar Grove Ave.
      </li>
      <li class="contact-item">
        <svg class="contact-icon" viewBox="0 0 24 24" fill="none" stroke="#2b5d9c" stroke-width="1.4"><circle cx="12" cy="12" r="11"/><path d="M8.5 7l2 2.5-1.2 1.3c.8 1.6 1.9 2.7 3.4 3.4l1.3-1.2 2.5 2-1.2 1.6c-3.8-.4-7.6-4.2-8-8z" fill="#2b5d9c" stroke="none"/></svg>
        044 555 21 40
      </li>
      <li class="contact-item">
        <svg class="contact-icon" viewBox="0 0 24 24" fill="none" stroke="#2b5d9c" stroke-width="1.4"><circle cx="12" cy="12" r="11"/><rect x="8.5" y="6.5" width="7" height="4"/><rect x="6.5" y="10.5" width="11" height="5"/><rect x="8.5" y="13.5" width="7" height="4" fill="#fff"/></svg>
        044 555 21 41
      </li>
      <li class="contact-item">
        <svg class="contact-icon" viewBox="0 0 24 24" fill="none" stroke="#2b5d9c" stroke-width="1.4"><circle cx="12" cy="12" r="11"/><rect x="6.5" y="8" width="11" height="8"/><path d="M6.5 8l5.5 4.5L17.5 8"/></svg>
        contact@rtrestful.com
      </li>
      <li class="contact-item">
        <svg class="contact-icon" viewBox="0 0 24 24" fill="none" stroke="#2b5d9c" stroke-width="1.2"><circle cx="12" cy="12" r="11"/><circle cx="12" cy="12" r="6"/><ellipse cx="12" cy="12" rx="2.6" ry="6"/><path d="M6 12h12M7 9h10M7 15h10"/></svg>
        www.rtrestful.com
      </li>
    </ul>
  </section>
</body>
</html>
```